Open design - funky concepts for speed dating events website

We are looking for an initial design/concept only (no coding) for 2 pages of an in-development speed dating events website - www.quickmatchmeetups.example. Once we have selected a design we will likely then look to engage the winning designer (probably in a freelance project) to complete other areas of the design.

The specification is very open and we're interested to see designs featuring different layouts, colours and design features.

The 2 pages are:
1. Home Page - http://www.quickmatchmeetups.example
2. Event Listing Page - http://www.quickmatchmeetups.example/Dating-Event.aspx
- the taxonomy section currently on the left hand side may include more items

Both page designs need to include the items that appear on these pages but in no way need to follow the current design or layout - eg. a 'Next Speed Dating Events' section should appear on the home page but where it appears, how many items in the listing, amount of details, size of images etc can change. Other elements may also be added such as image rotators.

Some elements that are on the current website and will appear on all pages:
- social media bookmark links
- ad units - need to include room for advertising locations
- country chooser - events are currently only listed for the UK but the site will eventually be tailored for different countries so users need the ability to select the country site they would like to view

Some elements that aren't on the current website but that should appear:
- User rating system on event listings (eg. 4 out of 5 stars, 1 out of 10, 2 out of 3 'thumbs up')
- User comments/feedback on event listings
- Prominent 'book now' or 'book for this event' type link/button for events (home and events page) and 'visit website' link/button for online listings (home page)

As far as looks we'd like a clean, attractive, personable design. Obviously we'd like some more colour than is currently on the site but we do need users to be able to browse through events and read the details comfortably.

Other than that it's entirely open - we're happy for the designs to be quite funky or less so.

Some further information following some questions we've received:
- We would like to see all the elements on the current home page in home page designs as fitting it all in is part of the issue. Layout is not set however the priorities for display would be roughly as they are displayed currently. ie. the 'Next Speed Dating Events' section is most prominent, Recently Viewed listings are shown, 'All Upcoming Events' may be below the fold etc.
- We don't have a requirement for a logo on the site and this doesn't necessarily need to appear in designs - totally up to you - we're lookiing at the overall page designs.
- There may be many items in the 'All Upcoming Speed Dating Events' section which we would be including on the home page. Ideally designs would feature a way of displaying these but don't need to include all items

Thank you everyone who submitted to the contest! We had some great designs again and were really impressed with the quality.

Cheers
Rupert

Target Market(s)

Singles looking for speed dating events in their region or online dating websites.

Industry/Entity Type

Advertising

Requirements
Must have
• As in the overview we need the elements that currently appear on the pages.

```html
<!DOCTYPE html>
<html lang="en">
<head>
<meta charset="utf-8">
<title>Quick Match Meetups – Speed Dating Events</title>
<link href="https://fonts.googleapis.com/css2?family=Arimo:wght@400;700&display=swap" rel="stylesheet">
<style>
:root{
  --navy:#1559ab;
  --header:#1a62b6;
  --nav:#2a86d6;
  --nav-dark:#1e6fc0;
  --sky-top:#4fa9ea;
  --sky-bottom:#2e86d4;
  --white:#ffffff;
  --ink:#333333;
  --muted:#666666;
  --link:#1a6ec4;
  --heading:#2a7bc8;
  --red:#e0201b;
  --star:#f5b800;
  --grey-box:#e6e6e6;
}
*{box-sizing:border-box;margin:0;padding:0}
html,body{width:1020px;height:1200px;overflow:hidden}
body{font-family:"Arimo",Arial,sans-serif;color:var(--ink);position:relative;background:var(--white)}
.abs{position:absolute}

/* header */
.site-header{left:0;top:0;width:1020px;height:125px;background:var(--header)}
.brand{left:104px;top:70px;width:350px;font-size:17px;font-weight:700;color:var(--white);letter-spacing:.3px;white-space:nowrap}
.social-box{left:475px;top:68px;width:185px;height:57px;background:var(--nav-dark);box-shadow:0 0 6px rgba(0,0,0,.3);display:flex;align-items:center;justify-content:center;gap:8px}
.account-links{left:817px;top:92px;font-size:13px;font-weight:700;color:var(--white)}

/* hero */
.hero{left:0;top:125px;width:1020px;height:642px;background:radial-gradient(ellipse at 55% 0%,#8fd0f7 0%,var(--sky-top) 35%,var(--sky-bottom) 100%)}
.main-nav{left:85px;top:125px;height:28px;display:flex}
.main-nav a{display:block;height:28px;line-height:28px;padding:0 20px;font-size:11.5px;color:var(--white);text-decoration:none;background:linear-gradient(#3a96e0,#2278c8);border-right:1px solid #1a5fb0;text-transform:uppercase}
.main-nav a.current{background:linear-gradient(#2a6fbd,#1a55a0);font-weight:700}
.online-count{left:718px;top:127px;width:217px;height:42px;background:var(--white);border-radius:0 0 4px 4px;color:var(--navy);font-size:13.5px;font-weight:700;text-align:center;line-height:17px;padding-top:4px}
.online-count .num{color:var(--red)}

.section-title{font-size:13.5px;font-weight:700;color:var(--white)}
.register-title{left:105px;top:198px;color:var(--navy)}
.field-label{font-size:11px;font-weight:700;color:var(--white)}
.field{width:160px;height:22px;border-radius:4px;background:linear-gradient(#e6eaee,#fafafa);border:1px solid #b9c6d3}
.btn{border-radius:4px;background:linear-gradient(#5cb6f0,#1d72c6);color:var(--white);font-weight:700;font-size:13px;text-align:center;box-shadow:0 1px 2px rgba(0,0,0,.35)}
.divider{left:382px;top:170px;width:1px;height:175px;background:rgba(255,255,255,.35)}
.welcome-title{left:425px;top:198px;font-size:14px;font-weight:700;color:#4a6a8a}
.welcome-title span{color:var(--navy)}
.welcome-text{left:425px;top:230px;width:470px;font-size:11px;line-height:15.5px;color:#1f3a55}

.event-card{width:155px;height:104px;border:2px solid var(--white);border-radius:3px;overflow:hidden;box-shadow:0 2px 4px rgba(0,0,0,.3)}
.event-photo{position:absolute;inset:0}
.photo-a{background:linear-gradient(135deg,#8a5a22,#c9952e 45%,#5b3a1a)}
.photo-b{background:linear-gradient(135deg,#1f4f6a,#3a8fb0 50%,#24384a)}
.photo-c{background:linear-gradient(135deg,#3a3a3a,#b98a6a 50%,#2a2a2a)}
.card-caption{position:absolute;left:0;bottom:0;width:100%;height:20px;background:rgba(0,0,0,.55);color:var(--white);font-size:11px;line-height:20px;padding-left:6px}
.rate{width:155px;text-align:center;font-size:11px;color:var(--white)}
.stars{width:155px;display:flex;justify-content:center;gap:2px}
.view-more{font-size:12px;color:#cfe9ff;line-height:14px;display:flex;align-items:center;gap:4px}
.v-line{width:1px;background:rgba(255,255,255,.6)}

.member{width:68px;height:68px;border:2px solid var(--white);box-shadow:0 1px 3px rgba(0,0,0,.3)}
.m1{background:linear-gradient(#2a2a2a,#b89a7a)}
.m2{background:linear-gradient(#3a1a3a,#c06aa0)}
.m3{background:linear-gradient(#3a5a2a,#8aa86a)}
.m4{background:linear-gradient(#2a3a4a,#a8a0a0)}
.m5{background:linear-gradient(#4a2a2a,#c89a8a)}
.m6{background:linear-gradient(#1a1a1a,#e0c0d0)}
.member-search{left:713px;top:670px;width:160px;height:22px;border-radius:4px;background:linear-gradient(#e6eaee,#fafafa);border:1px solid #b9c6d3;font-size:10.5px;color:#999;padding:4px 6px}

/* lower */
.news-title{left:105px;top:788px;font-size:13.5px;font-weight:700;color:var(--heading)}
.news-box{left:105px;top:808px;width:223px;height:189px;background:var(--grey-box);border-radius:6px;padding:16px 12px 0 18px}
.news-item{font-size:10.5px;line-height:14.5px;margin-bottom:11px;color:var(--ink)}
.news-item .date{color:var(--link);text-decoration:underline;display:block}
.news-item a{color:var(--link)}
.partner{width:150px}
.partner-mark{height:52px;display:flex;align-items:center;gap:6px;font-size:16px;font-weight:700;color:var(--link)}
.partner-mark .sq{width:18px;height:18px;background:var(--link);border-radius:3px}
.partner p{font-size:10.5px;line-height:15px;color:var(--ink);margin-top:16px;height:64px}
.partner a{font-size:10.5px;color:var(--link);display:block;margin-top:10px}
.ad-banner{left:107px;top:1021px;width:550px;height:85px;border:2px solid var(--link);display:flex;align-items:center;padding:0 16px;gap:18px}
.ad-art{width:80px;height:60px;background:linear-gradient(135deg,#c8d8e8,#7a9ab8)}
.ad-text{font-size:12.5px;font-weight:700;font-style:italic;color:#555;line-height:16px;width:300px}
.ad-mark{font-size:18px;font-weight:700;color:#555;display:flex;align-items:center;gap:6px}
.ad-mark .dot{width:12px;height:12px;border-radius:50%;background:var(--red)}
.testimonial{left:697px;top:1000px;width:230px}
.testimonial h3{font-size:14px;font-weight:400;color:#b0b0b0}
.testimonial h3 span{font-size:24px;color:#b0b0b0;font-family:Georgia,serif;margin-right:8px}
.testimonial p{font-size:9.5px;line-height:15px;color:#777;margin:8px 0 0 17px}
.testimonial .close{text-align:right;font-size:24px;color:#b0b0b0;font-family:Georgia,serif;line-height:14px}

.site-footer{left:0;top:1145px;width:1020px;height:55px;background:var(--navy);color:var(--white);font-size:10.5px}
.site-footer .copy{position:absolute;left:94px;top:21px}
.site-footer .legal{position:absolute;right:94px;top:21px}
.site-footer .legal a{color:var(--white);text-decoration:underline}
</style>
</head>
<body>

<header class="abs site-header"></header>
<div class="abs brand">QUICKMATCHMEETUPS.EXAMPLE</div>
<div class="abs social-box" aria-label="Social media links">
  <svg width="30" height="30" role="img" aria-label="Social link"><rect width="30" height="30" rx="5" fill="#3f67b0"/></svg>
  <svg width="30" height="30" role="img" aria-label="Social link"><rect width="30" height="30" rx="5" fill="#45b5e8"/></svg>
  <svg width="30" height="30" role="img" aria-label="Social link"><rect width="30" height="30" rx="5" fill="#2f7fb8"/></svg>
  <svg width="30" height="30" role="img" aria-label="Social link"><rect width="30" height="30" rx="5" fill="#3d8ee0"/></svg>
  <svg width="30" height="30" role="img" aria-label="Social link"><circle cx="15" cy="15" r="14" fill="#e0a020"/></svg>
</div>
<div class="abs account-links">Sign In &nbsp;|&nbsp; Register</div>

<section class="abs hero"></section>
<nav class="abs main-nav">
  <a class="current">Home</a><a>Online Dating</a><a>Dating Events</a><a>Event Providers</a><a>Event Venues</a>
</nav>
<div class="abs online-count"><span class="num">8,916</span> Singles Online Now!<br>Available to Speed Date</div>

<h2 class="abs section-title register-title">Register for updates</h2>
<label class="abs field-label" style="left:106px;top:236px">Location</label>
<div class="abs field" style="left:168px;top:230px"></div>
<label class="abs field-label" style="left:122px;top:270px">Email</label>
<div class="abs field" style="left:168px;top:264px"></div>
<div class="abs btn" style="left:258px;top:295px;width:70px;height:23px;line-height:23px">Sign Up</div>

<div class="abs divider"></div>
<h1 class="abs welcome-title">Welcome to <span>quickmatchmeetups.example</span></h1>
<p class="abs welcome-text">Lorem ipsum dolor sit amet, consectetur adipisicing elit, sed do eiusmod tempor incididunt ut labore et dolore magna aliqua. Ut enim ad minim veniam, quis nostrud exercitation ullamco laboris nisi ut aliquip ex ea commodo consequat.</p>
<div class="abs btn" style="left:425px;top:294px;width:72px;height:24px;line-height:24px">Read &gt;&gt;</div>

<h2 class="abs section-title" style="left:105px;top:375px">Next Speed Dating Events</h2>
<div class="abs event-card" style="left:105px;top:404px"><div class="event-photo photo-a" role="img" aria-label="Photo of a speed dating event in a bar"></div><div class="card-caption">Click to Book this Event</div></div>
<div class="abs event-card" style="left:270px;top:404px"><div class="event-photo photo-b" role="img" aria-label="Photo of singles at a club night"></div><div class="card-caption">Click to Book this Event</div></div>
<div class="abs event-card" style="left:435px;top:404px"><div class="event-photo photo-c" role="img" aria-label="Photo of a group of friends smiling"></div><div class="card-caption">Click to Book this Event</div></div>
<div class="abs rate" style="left:105px;top:518px">Rate this event</div>
<div class="abs rate" style="left:270px;top:518px">Rate this event</div>
<div class="abs rate" style="left:435px;top:518px">Rate this event</div>
<div class="abs v-line" style="left:598px;top:404px;height:104px"></div>
<div class="abs view-more" style="left:604px;top:440px">
  <svg width="24" height="30"><polygon points="0,8 12,8 12,0 24,15 12,30 12,22 0,22" fill="#fff"/></svg>
  <span>View<br>More &gt;&gt;</span>
</div>

<h2 class="abs section-title" style="left:105px;top:566px">Last Speed Dating Events</h2>
<div class="abs event-card" style="left:105px;top:596px"><div class="event-photo photo-a" role="img" aria-label="Photo of a speed dating event in a bar"></div><div class="card-caption">View Gallery</div></div>
<div class="abs event-card" style="left:270px;top:596px"><div class="event-photo photo-b" role="img" aria-label="Photo of singles at a club night"></div><div class="card-caption">View Gallery</div></div>
<div class="abs event-card" style="left:435px;top:596px"><div class="event-photo photo-c" role="img" aria-label="Photo of a group of friends smiling"></div><div class="card-caption">View Gallery</div></div>
<div class="abs rate" style="left:105px;top:710px">Rate this event</div>
<div class="abs rate" style="left:270px;top:710px">Rate this event</div>
<div class="abs rate" style="left:435px;top:710px">Rate this event</div>
<div class="abs v-line" style="left:598px;top:596px;height:104px"></div>
<div class="abs view-more" style="left:604px;top:632px">
  <svg width="24" height="30"><polygon points="0,8 12,8 12,0 24,15 12,30 12,22 0,22" fill="#fff"/></svg>
  <span>View<br>More &gt;&gt;</span>
</div>

<svg width="0" height="0" style="position:absolute">
  <defs>
    <polygon id="star" points="6,0 7.8,4 12,4.3 8.8,7.1 9.8,11.5 6,9.2 2.2,11.5 3.2,7.1 0,4.3 4.2,4"/>
  </defs>
</svg>
<div class="abs stars" style="left:105px;top:535px"><svg width="68" height="12"><use href="#star" fill="#f5b800"/><use href="#star" x="14" fill="#f5b800"/><use href="#star" x="28" fill="#f5b800"/><use href="#star" x="42" fill="#fff"/><use href="#star" x="56" fill="#fff"/></svg></div>
<div class="abs stars" style="left:270px;top:535px"><svg width="68" height="12"><use href="#star" fill="#f5b800"/><use href="#star" x="14" fill="#f5b800"/><use href="#star" x="28" fill="#f5b800"/><use href="#star" x="42" fill="#f5b800"/><use href="#star" x="56" fill="#fff"/></svg></div>
<div class="abs stars" style="left:435px;top:535px"><svg width="68" height="12"><use href="#star" fill="#f5b800"/><use href="#star" x="14" fill="#f5b800"/><use href="#star" x="28" fill="#f5b800"/><use href="#star" x="42" fill="#fff"/><use href="#star" x="56" fill="#fff"/></svg></div>
<div class="abs stars" style="left:105px;top:727px"><svg width="68" height="12"><use href="#star" fill="#f5b800"/><use href="#star" x="14" fill="#f5b800"/><use href="#star" x="28" fill="#f5b800"/><use href="#star" x="42" fill="#fff"/><use href="#star" x="56" fill="#fff"/></svg></div>
<div class="abs stars" style="left:270px;top:727px"><svg width="68" height="12"><use href="#star" fill="#f5b800"/><use href="#star" x="14" fill="#f5b800"/><use href="#star" x="28" fill="#f5b800"/><use href="#star" x="42" fill="#f5b800"/><use href="#star" x="56" fill="#fff"/></svg></div>
<div class="abs stars" style="left:435px;top:727px"><svg width="68" height="12"><use href="#star" fill="#f5b800"/><use href="#star" x="14" fill="#f5b800"/><use href="#star" x="28" fill="#f5b800"/><use href="#star" x="42" fill="#fff"/><use href="#star" x="56" fill="#fff"/></svg></div>

<h2 class="abs section-title" style="left:713px;top:375px">Members Online</h2>
<div class="abs member m1" style="left:713px;top:404px" role="img" aria-label="Member profile photo"></div>
<div class="abs member m2" style="left:785px;top:404px" role="img" aria-label="Member profile photo"></div>
<div class="abs member m3" style="left:857px;top:404px" role="img" aria-label="Member profile photo"></div>
<div class="abs member m4" style="left:713px;top:492px" role="img" aria-label="Member profile photo"></div>
<div class="abs member m5" style="left:785px;top:492px" role="img" aria-label="Member profile photo"></div>
<div class="abs member m6" style="left:857px;top:492px" role="img" aria-label="Member profile photo"></div>
<div class="abs member m6" style="left:713px;top:580px" role="img" aria-label="Member profile photo"></div>
<div class="abs member m1" style="left:785px;top:580px" role="img" aria-label="Member profile photo"></div>
<div class="abs member m4" style="left:857px;top:580px" role="img" aria-label="Member profile photo"></div>
<div class="abs member-search">Search for a member..</div>
<div class="abs btn" style="left:888px;top:670px;width:37px;height:22px;line-height:22px;font-size:11px">GO</div>

<h2 class="abs news-title">News &amp; Events</h2>
<div class="abs news-box">
  <div class="news-item"><span class="date">Saturday 25 September</span>Dating news story summary covering a few lines... <a>Read full article</a></div>
  <div class="news-item"><span class="date">Saturday 23 September</span>Dating news story summary covering a few lines... <a>Read full article</a></div>
  <div class="news-item"><span class="date">Saturday 19 September</span>Dating news story summary covering a few lines... <a>Read full article</a></div>
</div>

<div class="abs partner" style="left:380px;top:805px">
  <div class="partner-mark"><span class="sq"></span>Partner Pairing</div>
  <p>Partner Pairing is a premium dating and events organisation for professionals.</p>
  <a>View website...</a>
</div>
<div class="abs partner" style="left:562px;top:805px">
  <div class="partner-mark"><span class="sq"></span>Spark &amp; Chat</div>
  <p>Spark &amp; Chat is an international casual dating site where everyone can make new friends, communicate.</p>
  <a>View website...</a>
</div>
<div class="abs partner" style="left:746px;top:805px">
  <div class="partner-mark"><span class="sq"></span>KinMatch</div>
  <p>KinMatch is the premier Jewish singles community online. KinMatch has been building the Jewish community..</p>
  <a>View website...</a>
</div>

<div class="abs ad-banner">
  <div class="ad-art" role="img" aria-label="Advert illustration of event brochures"></div>
  <div class="ad-text">Take your MICE event to a higher level in Hong Kong - Asia's premier MICE destination.</div>
  <div class="ad-mark"><span class="dot"></span>Harbourline</div>
</div>

<div class="abs testimonial">
  <h3><span>&ldquo;</span>testimonials</h3>
  <p>In November 2002 I participated in my first and only SpeedDating event. That night, I met Clara, and we've been together ever since.<br>Thanks,<br>Dennis</p>
  <div class="close">&rdquo;</div>
</div>

<footer class="abs site-footer">
  <div class="copy">Copyright Notice © 2010 quickmatchmeetups.example. All rights reserved.</div>
  <div class="legal"><a>Terms &amp; Conditions</a> &nbsp;|&nbsp; <a>Privacy Policy</a> &nbsp;|&nbsp; <a>Legal Disclaimer</a></div>
</footer>

</body>
</html>
```